DUVNA Powerpoint Template

A powerpoint template for our new brand of private label components which are built for us in Asia. We are looking for a fresh design for our powerpoint template. Note the subtle overlay of the fox in our theme. We like this as it implies quickness. Do not overuse the fox theme. It needs to be very subtle if used.

Our products include High performance passive RF and Fiber components and cable solutions for the wireless industry. Our comprehensive product portfolios include both general and low PIM grades and are widely used for cellular towers and in-building DAS systems as well as in the wireless research and development labs.

Common models include:
Filters
Diplexers, triplexers and 5plexers
Splitters and combiners
Signal tappers
Couplers
Terminations load and attenuators
Jumper cables and testing cables assemblies
Fiber Splice Trays
Patch Panels
Fiber Jumpers & Adapters

```html
<!DOCTYPE html>
<html lang="en">
<head>
<meta charset="UTF-8">
<title>DUVNA – Project Slide</title>
<link href="https://fonts.googleapis.com/css2?family=Roboto+Condensed:wght@400;700&family=Arimo:wght@400&family=Carlito:wght@400;700&display=swap" rel="stylesheet">
<style>
  :root {
    --brand-red: #dd0000;
    --brand-red-light: #ff4242;
    --ink: #111111;
    --body-grey: #6b6b6b;
    --tint: #fdf1f2;
    --tint-soft: #ffffff;
    --rule: #f3c9cd;
    --grey-light: #bfbfbf;
    --grey-mid: #7f7f7f;
    --grey-dark: #595959;
    --white: #ffffff;
  }
  html, body {
    margin: 0;
    padding: 0;
    width: 1200px;
    height: 900px;
    overflow: hidden;
    background: var(--white);
  }
  .slide {
    position: relative;
    width: 1200px;
    height: 900px;
    overflow: hidden;
    background: var(--white);
  }
  .slide-header {
    position: absolute;
    left: 0; top: 0;
    width: 1200px;
    height: 84px;
    background: var(--white);
    border-bottom: 1.5px solid var(--rule);
    box-sizing: border-box;
  }
  .project-title {
    position: absolute;
    left: 33px;
    top: 12px;
    margin: 0;
    font-family: "Roboto Condensed", "Arial Narrow", sans-serif;
    font-weight: 400;
    font-size: 51px;
    line-height: 60px;
    color: var(--ink);
  }
  .project-title .accent { color: var(--brand-red); }
  .brand-name {
    position: absolute;
    right: 14px;
    top: 16px;
    display: flex;
    align-items: center;
    gap: 10px;
    font-family: "Roboto Condensed", "Arial Narrow", sans-serif;
    font-weight: 700;
    font-size: 46px;
    line-height: 50px;
    letter-spacing: 3px;
    color: var(--brand-red);
  }
  .brand-mark {
    width: 18px;
    height: 18px;
    background: var(--brand-red);
  }
  .content-area {
    position: absolute;
    left: 0; top: 85px;
    width: 1200px;
    height: 753px;
    background: var(--tint);
  }
  .theme-motif {
    position: absolute;
    left: 0; top: 85px;
    width: 1200px;
    height: 753px;
    background:
      radial-gradient(ellipse 520px 300px at 980px 560px, rgba(255,255,255,0.85), rgba(255,255,255,0) 70%),
      radial-gradient(ellipse 420px 160px at 150px 330px, rgba(255,255,255,0.55), rgba(255,255,255,0) 70%);
  }
  .content-title {
    position: absolute;
    left: 69px;
    top: 194px;
    margin: 0;
    font-family: "Roboto Condensed", "Arial Narrow", sans-serif;
    font-weight: 400;
    font-size: 44px;
    line-height: 52px;
    color: var(--brand-red);
  }
  .content-body {
    position: absolute;
    left: 71px;
    top: 252px;
    width: 490px;
    font-family: "Arimo", Arial, sans-serif;
    font-size: 20.5px;
    line-height: 33px;
    color: var(--body-grey);
  }
  .content-body p { margin: 0 0 33px 0; }
  .pie-chart {
    position: absolute;
    left: 0; top: 0;
    width: 1200px;
    height: 900px;
  }
  .slice-label {
    font-family: "Carlito", Calibri, sans-serif;
    font-weight: 700;
    font-size: 11.5px;
    text-anchor: middle;
  }
  .slice-label.dark { fill: #222222; }
  .slice-label.light { fill: var(--white); }
  .footer-rule {
    position: absolute;
    left: 0; top: 838px;
    width: 1200px;
    height: 5px;
    background: var(--ink);
  }
  .slide-footer {
    position: absolute;
    left: 0; top: 845px;
    width: 1200px;
    height: 55px;
    background: var(--brand-red);
    font-family: "Carlito", Calibri, sans-serif;
    font-size: 20px;
    color: var(--white);
  }
  .copyright {
    position: absolute;
    left: 19px;
    top: 15px;
  }
  .page-number {
    position: absolute;
    right: 16px;
    top: 15px;
    font-weight: 700;
  }
</style>
</head>
<body>
<div class="slide">
  <header class="slide-header">
    <h1 class="project-title"><span class="accent">Project</span> Title Here</h1>
    <div class="brand-name"><span class="brand-mark"></span>DUVNA</div>
  </header>

  <div class="content-area"></div>
  <div class="theme-motif" role="img" aria-label="Very faint fox motif in the slide background"></div>

  <h2 class="content-title">Content Title Here</h2>
  <div class="content-body">
    <p>Sub Content Here Sub Content Here Sub Content Here Sub Content Here Sub Content Here Sub Content Here Sub Content Here Sub Content Here Sub Content Here Sub Content Here Sub Content Here</p>
    <p>Sub Content Here Sub Content Here Sub Content Here Sub Content Here Sub Content Here Sub Content Here Sub Content Here Sub Content Here Sub Content Here Sub Content Here.</p>
  </div>

  <svg class="pie-chart" viewBox="0 0 800 600" aria-label="Pie chart with five segments">
    <g stroke="#ffffff" stroke-width="1.2" stroke-linejoin="round">
      <path d="M591 310 L591 157 A153 153 0 0 1 681 186.2 Z" fill="var(--grey-light)"/>
      <path d="M591 310 L681 186.2 A153 153 0 0 1 735.7 359.8 Z" fill="var(--brand-red-light)"/>
      <path d="M591 310 L735.7 359.8 A153 153 0 0 1 447.2 362.3 Z" fill="var(--brand-red)"/>
      <path d="M591 310 L447.2 362.3 A153 153 0 0 1 505.4 183.2 Z" fill="var(--grey-dark)"/>
      <path d="M591 310 L505.4 183.2 A153 153 0 0 1 591 157 Z" fill="var(--grey-mid)"/>
    </g>
    <circle cx="593" cy="308" r="26" fill="#ffffff" stroke="var(--brand-red)" stroke-width="3"/>

    <text class="slice-label dark" x="622" y="200">Lorem</text>
    <text class="slice-label dark" x="622" y="216">ipsum</text>
    <text class="slice-label dark" x="622" y="232">dolor</text>

    <text class="slice-label light" x="562" y="200">Lorem</text>
    <text class="slice-label light" x="562" y="216">ipsum</text>
    <text class="slice-label light" x="562" y="232">dolor</text>

    <text class="slice-label dark" x="684" y="288">Lorem ipsum</text>
    <text class="slice-label dark" x="682" y="304">dolor</text>

    <text class="slice-label light" x="506" y="284">Lorem ipsum dolor</text>
    <text class="slice-label light" x="506" y="300">Lorem ipsum dolor</text>

    <text class="slice-label light" x="586" y="385">Lorem ipsum dolor</text>
    <text class="slice-label light" x="586" y="402">Lorem ipsum dolor</text>
  </svg>

  <div class="footer-rule"></div>
  <footer class="slide-footer">
    <span class="copyright">Copyright text here</span>
    <span class="page-number">Page : 01</span>
  </footer>
</div>
</body>
</html>
```